Quellora business card design

create modern and tech looking business card that is clean but effectively communciates that we are a cloud communications company.
Should have at minimum:
Employee Name
Postion
Phone Number
Email
website
Contact Information for Business Card
create modern and tech looking business card that is clean but effectively communciates that we are a cloud communications company. We have two logo color schemes (attached) so would like to see designs both ways
Should have at minimum:
Employee Name
Postion
Phone Number
Email
website

```html
<!DOCTYPE html>
<html lang="en">
<head>
<meta charset="utf-8">
<title>Quellora business card</title>
<link href="https://fonts.googleapis.com/css2?family=Roboto:wght@400;500&family=Roboto+Condensed:wght@500&display=swap" rel="stylesheet">
<style>
  :root {
    --stage: #2b2b2b;
    --card: #f5f5f5;
    --purple: #5f2c8f;
    --cyan: #29b6d9;
    --ink: #4a4a4a;
    --text: #444444;
  }
  html, body {
    margin: 0;
    padding: 0;
    width: 1200px;
    height: 960px;
    overflow: hidden;
    background: var(--stage);
    font-family: "Roboto", Arial, sans-serif;
  }
  .canvas { position: relative; width: 1200px; height: 960px; }
  .card {
    position: absolute;
    width: 600px;
    height: 342px;
    background: var(--card);
    overflow: hidden;
  }
  .card--front { left: 314px; top: 113px; }
  .card--back { left: 311px; top: 472px; }

  .pixel-field { position: absolute; left: 0; top: 0; width: 372px; height: 342px; }

  .wordmark {
    position: absolute;
    margin: 0;
    font-family: "Roboto", Arial, sans-serif;
    font-weight: 500;
    color: var(--ink);
    letter-spacing: 3px;
    text-transform: uppercase;
    line-height: 1;
  }
  .card--front .wordmark { left: 340px; top: 123px; font-size: 30px; }

  .holder { position: absolute; left: 340px; top: 180px; }
  .holder__name {
    margin: 0;
    font-family: "Roboto Condensed", Arial, sans-serif;
    font-weight: 500;
    font-size: 21px;
    color: var(--purple);
    text-transform: uppercase;
    line-height: 1.1;
  }
  .holder__role {
    margin: 3px 0 0;
    font-size: 15px;
    color: var(--cyan);
    text-transform: uppercase;
  }
  .contacts {
    position: absolute;
    left: 340px;
    top: 238px;
    margin: 0;
    padding: 0;
    list-style: none;
    font-size: 14px;
    color: var(--text);
  }
  .contacts li { display: flex; align-items: center; height: 19.5px; }
  .contacts svg { width: 12px; height: 12px; margin-right: 10px; fill: var(--purple); }

  .brand-lockup {
    position: absolute;
    left: 0; right: 0; top: 0; bottom: 0;
    display: flex;
    align-items: center;
    justify-content: center;
    gap: 18px;
  }
  .brand-lockup__square { width: 34px; height: 34px; background: var(--purple); }
  .card--back .wordmark { position: static; font-size: 44px; letter-spacing: 4px; }
</style>
</head>
<body>
<main class="canvas">
  <section class="card card--front">
    <svg class="pixel-field" viewBox="0 0 372 342" role="img" aria-label="Decorative pattern of purple and cyan pixel squares fading toward the right">
      <defs>
        <linearGradient id="pixelTone" x1="0" y1="0" x2="1" y2="1">
          <stop offset="0" stop-color="#5f2c8f" stop-opacity="0.85"/>
          <stop offset="1" stop-color="#29b6d9" stop-opacity="0.55"/>
        </linearGradient>
      </defs>
      <polygon fill="url(#pixelTone)" points="0,0 346,0 346,18 372,18 372,48 290,48 290,160 245,160 245,180 192,180 192,260 185,285 108,285 108,315 25,315 25,342 0,342"/>
    </svg>

    <h1 class="wordmark">Quellora</h1>

    <div class="holder">
      <p class="holder__name">Dana Whitfield</p>
      <p class="holder__role">CEO/Founder</p>
    </div>

    <ul class="contacts">
      <li><svg viewBox="0 0 24 24"><path d="M6.6 10.8a15 15 0 0 0 6.6 6.6l2.2-2.2c.3-.3.7-.4 1-.2 1.1.4 2.3.6 3.6.6.6 0 1 .4 1 1V20c0 .6-.4 1-1 1A17 17 0 0 1 3 4c0-.6.4-1 1-1h3.5c.6 0 1 .4 1 1 0 1.3.2 2.5.6 3.6.1.3 0 .7-.2 1z"/></svg>555 201 4836</li>
      <li><svg viewBox="0 0 24 24"><path d="M2 5h20v14H2z M4 7v.5l8 5 8-5V7l-8 5z" fill-rule="evenodd"/></svg>dana@quellora.com</li>
      <li><svg viewBox="0 0 24 24"><path d="M12 2a10 10 0 1 0 0 20 10 10 0 0 0 0-20zm-1 17.9A8 8 0 0 1 4.2 10L9 15v1c0 1.1.9 2 2 2zm6.9-2.5A2 2 0 0 0 16 16h-1v-3c0-.6-.4-1-1-1H8v-2h2c.6 0 1-.4 1-1V7h2c1.1 0 2-.9 2-2v-.4a8 8 0 0 1 2.9 12.8z"/></svg>www.quellora.com</li>
    </ul>
  </section>

  <section class="card card--back">
    <div class="brand-lockup">
      <span class="brand-lockup__square"></span>
      <h2 class="wordmark">Quellora</h2>
    </div>
  </section>
</main>
</body>
</html>
```